Security Services Business Card

Looking for a clean modern style business card design for a residential and commercial security solutions provider. We install and service the following
security alarm, access control, video surveillance and fire alarm. Attached are the front and back of our current business cards in PSD file format.

Target Market(s)

Security alarm clients in the commercial and residential markets

Industry/Entity Type

Security Service

Contact Information for Business Card

We are open to designers suggestion and or design ideas.

Font styles to use
Serif
Sans Serif

Colors
3276b5
33a6d7
fffefd

Requirements
Must have
• Must have company logo , first and last name , phone number , web and email address, ect....

```html
<!DOCTYPE html>
<html lang="en">
<head>
<meta charset="utf-8">
<title>Brightward Systems – Business Card</title>
<link href="https://fonts.googleapis.com/css2?family=Montserrat:wght@700&family=Roboto:wght@400;700&display=swap" rel="stylesheet">
<style>
  :root {
    --brand-blue: #33a6d7;
    --deep-blue: #3276b5;
    --paper: #fffefd;
    --ink: #3a3a3a;
    --backdrop: #9a9a9a;
    --logo-tint: #bfe3f5;
  }
  * { margin: 0; padding: 0; box-sizing: border-box; }
  html, body { width: 1200px; height: 992px; overflow: hidden; }
  body {
    background: var(--backdrop);
    font-family: "Roboto", Arial, sans-serif;
    position: relative;
  }
  .card {
    position: absolute;
    left: 250px;
    width: 700px;
    height: 400px;
    box-shadow: 0 10px 30px rgba(0,0,0,0.25);
  }
  .card-front { top: 66px; background: var(--paper); }
  .card-back { top: 526px; background: var(--brand-blue); border-bottom: 4px solid var(--deep-blue); }

  .person { position: absolute; left: 64px; top: 58px; }
  .person-name {
    font-family: "Montserrat", Arial, sans-serif;
    font-weight: 700; font-size: 25px; color: var(--brand-blue);
    letter-spacing: 0.5px;
  }
  .person-title { font-size: 20px; color: var(--ink); margin-top: 2px; }

  .contact { position: absolute; left: 64px; top: 158px; font-size: 19px; line-height: 25px; color: var(--ink); }
  .contact-company { color: var(--brand-blue); }
  .contact-row { display: flex; align-items: center; gap: 8px; }
  .contact-row svg { width: 17px; height: 17px; flex: none; }

  .brand-mark {
    position: absolute; right: 90px; bottom: 70px;
    display: flex; align-items: center; gap: 12px;
  }
  .brand-dot { width: 18px; height: 18px; border-radius: 50%; background: var(--brand-blue); }
  .brand-name { font-weight: 700; font-size: 46px; color: var(--brand-blue); }

  .back-brand {
    position: absolute; left: 0; right: 0; top: 110px;
    display: flex; justify-content: center; align-items: center; gap: 20px;
  }
  .back-brand .brand-dot { width: 30px; height: 30px; background: var(--logo-tint); }
  .back-brand .brand-name { font-size: 96px; color: var(--logo-tint); }

  .services {
    position: absolute; left: 0; right: 0; bottom: 50px;
    text-align: center; color: var(--paper); font-size: 21px; letter-spacing: 0.3px;
  }
  .services span::before { content: "• "; }
  .services span + span { margin-left: 14px; }
</style>
</head>
<body>
  <section class="card card-front">
    <div class="person">
      <div class="person-name">MARCUS ELLERY</div>
      <div class="person-title">Managing Director</div>
    </div>
    <div class="contact">
      <div class="contact-company">Brightward Systems, LLC</div>
      <div>4180 Harbor Point Suite #212</div>
      <div>Lakeview, Ohio 44012</div>
      <div class="contact-row">
        <svg viewBox="0 0 24 24" aria-hidden="true"><path fill="#33a6d7" d="M6.6 10.8a15 15 0 0 0 6.6 6.6l2.2-2.2c.3-.3.7-.4 1-.2 1.1.4 2.3.6 3.6.6.6 0 1 .4 1 1V20c0 .6-.4 1-1 1A17 17 0 0 1 3 4c0-.6.4-1 1-1h3.5c.6 0 1 .4 1 1 0 1.3.2 2.5.6 3.6.1.3 0 .7-.2 1z"/></svg>
        555.014.2290 ext
      </div>
      <div class="contact-row">
        <svg viewBox="0 0 24 24" aria-hidden="true"><rect x="2" y="5" width="20" height="14" fill="#33a6d7"/><path d="M2 5l10 8 10-8" fill="none" stroke="#fffefd" stroke-width="1.6"/></svg>
        info@brightwardinfo.com
      </div>
      <div class="contact-row">
        <svg viewBox="0 0 24 24" aria-hidden="true"><circle cx="12" cy="12" r="10" fill="#33a6d7"/><path d="M2 12h20M12 2c3 3 3 17 0 20M12 2c-3 3-3 17 0 20" fill="none" stroke="#fffefd" stroke-width="1.3"/></svg>
        www.brightwardinfo.com
      </div>
    </div>
    <div class="brand-mark">
      <span class="brand-dot"></span>
      <span class="brand-name">Brightward</span>
    </div>
  </section>

  <section class="card card-back">
    <div class="back-brand">
      <span class="brand-dot"></span>
      <span class="brand-name">Brightward</span>
    </div>
    <div class="services">
      <span>Video Surveillance</span><span>Security Alarm</span><span>Fire Alarm</span><span>Access Control</span>
    </div>
  </section>
</body>
</html>
```